Trading company needs a non alcoholic beer Can design

We KLM are trading company , food Distributors in Africa -RD Congo/Kinshasa .We want to do a Private label non alcoholic beer 500ml can and need a design for this Project .
the Brand Name is : NUVA BREW
We want it to be similar NOT a copy of Velmora 0.0% can ( picture
attached ) as we want to respect the intellectual properties .so we prefer to use the same colors but more elegant ,modern style .
thanks.
THE DESIGN MUST STATE ITS A NON ALCOHOLIC BEER
PLZ SEARCH FOR VELMORA 0.0% MALT DRINK YOU WILL FIND 2 DESIGNS OLD AND NEW WE NEED SOMTHING SIMILAR TO THESE DESIGNS ,KINDLY USE SAME COLORS AND THE 0.0% SHOULD BE IN THE MIDDLE OF THE CAN .
Target Market(s)
THE PRODUCT WILL BE SOLD IN THE SUPERMASRKTS / MODERN TRADE

```html
<!DOCTYPE html>
<html lang="en">
<head>
<meta charset="utf-8">
<title>NUVA BREW – Non Alcoholic Beer Can Label</title>
<link rel="stylesheet" href="https://fonts.googleapis.com/css2?family=Montserrat:ital,wght@0,500;0,600;0,700;0,800;1,800;1,900&display=swap">
<style>
  :root {
    --backdrop: #e4e5e6;
    --can-silver: #ececed;
    --can-silver-edge: #d6d7d9;
    --label-red: #d8321e;
    --label-red-deep: #bf1f0e;
    --badge-blue: #1b388c;
    --ink-white: #ffffff;
    --hex-white: #fbfbfb;
  }
  html, body {
    margin: 0;
    padding: 0;
    width: 1026px;
    height: 1200px;
    overflow: hidden;
    background: var(--backdrop);
  }
  .label-canvas {
    display: block;
    width: 1026px;
    height: 1200px;
  }
  .label-text {
    font-family: "Montserrat", sans-serif;
    fill: var(--ink-white);
    text-anchor: middle;
  }
  .brand-name { font-weight: 700; font-size: 60px; }
  .brand-descriptor { font-weight: 500; font-size: 26px; letter-spacing: 0.5px; }
  .abv-figure {
    font-family: "Montserrat", sans-serif;
    font-style: italic;
    font-weight: 900;
    fill: var(--badge-blue);
    text-anchor: start;
  }
  .abv-number { font-size: 112px; }
  .abv-percent { font-size: 64px; }
  .abv-unit { font-size: 21px; font-weight: 800; }
  .tagline-small { font-weight: 700; font-size: 30px; }
  .tagline-large { font-weight: 800; font-size: 42px; letter-spacing: 1px; }
</style>
</head>
<body>
<svg class="label-canvas" viewBox="94 100 1126 1317" xmlns="http://www.w3.org/2000/svg" aria-labelledby="label-title">
  <title id="label-title">NUVA BREW non alcoholic beer, 0.0% alcohol, premium original</title>
  <defs>
    <linearGradient id="red-panel-shade" x1="0" y1="0" x2="1" y2="0">
      <stop offset="0" stop-color="var(--label-red-deep)"/>
      <stop offset="0.35" stop-color="var(--label-red)"/>
      <stop offset="0.7" stop-color="var(--label-red)"/>
      <stop offset="1" stop-color="var(--label-red-deep)"/>
    </linearGradient>
    <linearGradient id="silver-shade" x1="0" y1="0" x2="1" y2="0">
      <stop offset="0" stop-color="var(--can-silver-edge)"/>
      <stop offset="0.2" stop-color="var(--can-silver)"/>
      <stop offset="0.8" stop-color="var(--can-silver)"/>
      <stop offset="1" stop-color="var(--can-silver-edge)"/>
    </linearGradient>
  </defs>

  <g class="can-label">
    <rect class="label-body" x="385" y="150" width="545" height="1280" rx="14" fill="url(#silver-shade)"/>
    <rect class="red-column" x="445" y="190" width="415" height="1200" fill="url(#red-panel-shade)"/>

    <g class="brand-banner">
      <path d="M430 460 Q430 435 455 435 H850 Q875 435 875 460 V640 L652 715 L430 640 Z" fill="var(--badge-blue)"/>
      <text class="label-text brand-name" x="654" y="558" textLength="385" lengthAdjust="spacingAndGlyphs">NUVA BREW</text>
      <text class="label-text brand-descriptor" x="652" y="595">NON ALCOHOLIC</text>
      <text class="label-text brand-descriptor" x="652" y="631">BEER</text>
    </g>

    <g class="abv-badge">
      <path d="M650 780 L812 848 V982 L650 1050 L488 982 V848 Z" fill="var(--hex-white)"/>
      <text class="abv-figure abv-number" x="530" y="955" textLength="150" lengthAdjust="spacingAndGlyphs">0.0</text>
      <text class="abv-figure abv-percent" x="698" y="910" textLength="60" lengthAdjust="spacingAndGlyphs">%</text>
      <text class="abv-figure abv-unit" x="688" y="954">ALC.</text>
    </g>

    <g class="tagline">
      <text class="label-text tagline-small" x="652" y="1150">PREMIUM</text>
      <text class="label-text tagline-large" x="652" y="1198">ORIGINAL</text>
    </g>
  </g>
</svg>
</body>
</html>
```